Flyer-Design für Handelsunternehmen
Zielgruppe
Wir sind ein Handelsunternehmen für Produkte zur Ladungssicherung im Container.
Unsere Zielgruppe sind Speditionen, Stauer, Logistiker, Exporteure, Industrie & Handel.
Kernprodukte sind Stausäcke, Lashband, Container-Lashing, Container-Planen, Umreifungsband, Plomben sowie Halterungen von FRACHTOMIR®.
Gewünscht sind Flyer (& Broschüren) sowohl zu den einzelnen Produktgruppen wie auch als Gesamtübersicht
(Bilder und Textbeispiele auf www.KTlager57.de bzw. nach Rücksprache)
Der Flyer soll schwerpunktmäßig einen kurzen Überblick über die genannten Produktkategorien abbilden. Damit der Kunde (ausschließlich B2B) weiß, was wir anbieten.
Verkauf findet nicht nur über den Shop statt, sondern auch klassisch per Telefon, Fax und Vertriebsmitarbeiter.
Aufgabenstellung
Bilder und Textbeispiele auf www.KTlager57.de bzw. nach Rücksprache

```html
<!DOCTYPE html>
<html lang="de">
<head>
<meta charset="utf-8">
<title>Kramer &amp; Tessin – Broschüre Ladungssicherung</title>
<link rel="stylesheet" href="https://fonts.googleapis.com/css2?family=Barlow+Condensed:wght@400;500;600&family=Montserrat:wght@400;600;700&display=swap">
<style>
:root{
  --navy:#1d2e58;
  --blue:#2c53b0;
  --blue-soft:#3b62c4;
  --ink:#333a47;
  --grey-bg:#d9d9d9;
  --white:#ffffff;
  --rule:#e6e6e6;
}
*{box-sizing:border-box;margin:0;padding:0}
html,body{width:1200px;height:3676px;overflow:hidden}
body{position:relative;background:linear-gradient(90deg,var(--grey-bg) 0 922px,var(--white) 922px);font-family:"Montserrat",sans-serif;color:var(--ink)}
.abs{position:absolute}
.page{position:absolute;background:var(--white)}
.navy{background:var(--navy)}
.head{font-family:"Barlow Condensed",sans-serif;color:var(--blue);text-transform:uppercase;line-height:1}
.body-text{font-size:6.6px;line-height:1.32;color:var(--ink);text-align:justify}
.sub{font-size:8.2px;font-weight:700;color:var(--blue);margin:12px 0 3px}
.photo{position:absolute}
.pnum{position:absolute;font-size:7px;font-weight:700;color:var(--ink)}
.wordmark{font-family:"Barlow Condensed",sans-serif;color:var(--blue);font-size:13px;line-height:.95;font-weight:500;text-transform:uppercase}
.badge{position:absolute;width:26px;height:26px;background:var(--navy);color:var(--white);font-family:"Barlow Condensed",sans-serif;font-size:18px;display:flex;align-items:center;justify-content:center}
.caption{position:absolute;width:170px;font-size:6px;line-height:1.25;text-align:justify}
.caption b{font-size:8px;font-weight:600}
.value{position:absolute;color:var(--white);font-size:6.6px;line-height:1.2;text-align:center;width:120px}
.value b{display:block;font-size:7.5px}
</style>
</head>
<body>

<!-- Cover -->
<section class="page navy" style="left:57px;top:52px;width:410px;height:376px">
  <div class="wordmark abs" style="left:32px;top:50px">Kramer &amp; Tessin<br><span style="font-weight:400">Ladungssicherung</span></div>
</section>
<section class="page" style="left:57px;top:428px;width:410px;height:65px">
  <div class="head abs" style="left:32px;top:14px;font-size:21px;font-weight:400">Weltweit mit <b style="font-weight:600">Sicherheit</b><br>transportieren.</div>
</section>
<div class="photo" role="img" aria-label="Nächtliche Autobahnkreuzung mit Lichtspuren" style="left:57px;top:493px;width:410px;height:139px;background:linear-gradient(160deg,#0d1e3a,#1f4d86 45%,#4a7fbf 70%,#0e2444)"></div>

<!-- Spread 2 -->
<section class="page navy" style="left:57px;top:652px;width:410px;height:580px">
  <p class="head abs" style="left:20px;top:92px;width:370px;text-align:center;font-size:33px;font-weight:400;line-height:1.18">„Jedem Unternehmen die maßgeschneiderte Lösung zu seiner Problemstellung anbieten zu können und so individuell auf Kundenbedürfnisse zu reagieren.“</p>
  <div class="abs" style="left:197px;top:446px;width:16px;height:1px;background:var(--blue)"></div>
  <p class="abs" style="left:0;top:455px;width:410px;text-align:center;font-size:10px;color:var(--blue)">unsere philosophie</p>
</section>
<section class="page" style="left:467px;top:652px;width:410px;height:580px">
  <h2 class="head abs" style="right:18px;top:40px;font-size:25px;font-weight:500">Über uns</h2>
  <div class="body-text abs" style="left:18px;top:104px;width:150px">
    <p>Die Kramer &amp; Tessin GmbH wurde im Jahr 1996 gegründet.</p><br>
    <p>Wir vertreiben weltweit innovative Produkte zur Ladungssicherung. Wir stehen Ihnen mit Rat und Tat zur Seite, um werterhaltende Maßnahmen einzuleiten und anzuwenden.</p><br>
    <p>Wir schaffen Voraussetzungen, Ihre Waren durch individuelle Lösungen gegen sämtliche Arten von Transportschäden zu sichern. Wir zeigen Ihnen Möglichkeiten auf, Ihre Waren wirkungsvoll gegen auftretende mechanische und klimatische Transportbelastungen zu schützen. Wir gewährleisten Ihre Transportsicherheit, um Gefährdungen von Mitmenschen und Umwelt auszuschließen.</p><br>
    <p>Wir bieten Ihnen Services in Theorie und Praxis. Wir planen anhand Ihrer Anforderungsprofile Versandlösungen. Wir erarbeiten virtuelle Staupläne für Ihre Container. Wir stellen vor Ort unsere Produkte vor und arbeiten Ihre Mitarbeiter ein.</p><br>
    <p>Wir bieten Ihnen einen kompetenten und unkomplizierten Support.</p><br>
    <p>Als Systemlieferant für Verpackungs- und Supply-Chain-Lösungen ist die Kramer &amp; Tessin GmbH somit Ihr idealer Partner.</p>
  </div>
</section>
<div class="photo" role="img" aria-label="Blaue Containertür mit Gewichtsangaben" style="left:644px;top:808px;width:233px;height:370px;background:linear-gradient(135deg,#16335f,#2d5d9a 50%,#1a3a6b)"></div>

<!-- Spread 3: values & vision -->
<div class="photo" role="img" aria-label="Leuchtturm an felsiger Küste in der Abenddämmerung" style="left:57px;top:1260px;width:410px;height:578px;background:linear-gradient(180deg,#3152a6 0%,#4a6cc0 40%,#3a5aa8 60%,#253f82 100%)"></div>
<div class="photo" role="img" aria-label="Ruhiges Meer über Felsen in blauer Stunde" style="left:467px;top:1260px;width:410px;height:578px;background:linear-gradient(180deg,#2d55b4 0%,#4a76d0 45%,#6f97de 62%,#33569f 100%)"></div>
<svg class="abs" style="left:57px;top:1260px" width="410" height="578" viewBox="0 0 410 578">
  <g fill="none" stroke="#fff" stroke-width="1.2" stroke-dasharray="2 3">
    <path d="M80 190 A140 140 0 0 1 150 85"/>
    <path d="M270 85 A140 140 0 0 1 345 185"/>
    <path d="M345 260 A140 140 0 0 1 270 355"/>
    <path d="M150 360 A140 140 0 0 1 75 270"/>
  </g>
  <g fill="#fff">
    <path d="M150 85 l-7 0 l4 -6z"/><path d="M345 185 l-5 -5 l6 0z"/><path d="M270 355 l6 2 l-4 5z"/><path d="M75 270 l-3 7 l6 -1z"/>
  </g>
</svg>
<div class="head abs" style="left:212px;top:1447px;color:#fff;font-size:31px;font-weight:500;line-height:1">Unsere<br>Werte</div>
<div class="value" style="left:145px;top:1303px"><b>RESPEKT</b>Offen und ehrlich sein und sich integer verhalten fördert die Zusammenarbeit und ermöglicht es uns, unsere gemeinsamen Ziele zu verwirklichen.</div>
<div class="value" style="left:338px;top:1440px"><b>SPITZENLEISTUNG</b>Spitzenleistungen lassen sich nur erreichen, wenn wir uns ständig herausfordern, gesteckte Ziele sowie die Erwartungen unserer Kunden und Mitarbeiter zu übertreffen und unsere Ergebnisse zu verbessern.</div>
<div class="value" style="left:62px;top:1440px"><b>VERANTWORTUNG</b>Wir müssen unsere täglichen Aufgaben stets sorgfältig und achtsam erledigen. Dabei dürfen wir die Interessen unserer Kunden und unseres Unternehmens nie aus den Augen verlieren.</div>
<div class="value" style="left:200px;top:1575px"><b>INITIATIVE</b>Der Motor unserer Unternehmenskultur treibt uns in unserer täglichen Arbeit voran. Die Eigeninitiative kreativer Mitarbeiter in unserer Organisation hat unser Wachstum gefördert und ist unser Erfolgsgeheimnis.</div>
<div class="pnum" style="left:70px;top:1820px;color:#fff">5</div>
<h2 class="head abs" style="left:589px;top:1570px;color:#fff;font-size:38px;font-weight:600">Unsere Vision</h2>
<div class="abs" style="left:591px;top:1628px;width:272px;color:#fff;font-size:13.5px;line-height:1.15">
  <p style="margin-bottom:7px">Wir werden führend sein im nachhaltigen Wirtschaften!</p>
  <p style="margin-bottom:7px">Wir werden führend sein in unserem Handeln, damit es stets den höchsten wirtschaftlichen und ökologischen Standards entspricht!</p>
  <p>Wir werden führend sein, um unseren Kunden stets den bestmöglichen Nutzen zu bieten!</p>
</div>
<div class="pnum" style="left:864px;top:1820px;color:#fff">6</div>

<!-- Spread 4: products -->
<section class="page" style="left:57px;top:1856px;width:410px;height:580px">
  <p class="head abs" style="left:24px;top:36px;font-size:21px;font-weight:500">Produkte</p>
  <h2 class="head abs" style="left:24px;top:66px;font-size:40px;font-weight:500;line-height:.98">Womit wollen<br>Sie sichern?</h2>
  <div class="pnum" style="left:16px;top:562px">7</div>
</section>
<div class="photo" role="img" aria-label="Ratsche eines Spanngurts in Nahaufnahme" style="left:57px;top:2112px;width:246px;height:292px;background:linear-gradient(150deg,#4a4650,#8a7078 45%,#2f2c34)"></div>
<section class="page" style="left:467px;top:1856px;width:410px;height:580px">
  <div class="pnum" style="left:390px;top:562px">8</div>
</section>
<div class="photo" role="img" aria-label="Stausäcke zwischen Kartons" style="left:497px;top:1868px;width:150px;height:122px;background:linear-gradient(180deg,#cbb398,#a9896a)"></div>
<div class="badge" style="left:507px;top:1950px">1</div>
<div class="photo" role="img" aria-label="Gelber Industrieroboter im Container" style="left:683px;top:1868px;width:163px;height:122px;background:linear-gradient(180deg,#8a8c90,#c2ad3a 50%,#6f7075)"></div>
<div class="badge" style="left:697px;top:1950px">2</div>
<div class="photo" role="img" aria-label="Blaue Fässer im Container gesichert" style="left:497px;top:2006px;width:153px;height:112px;background:linear-gradient(180deg,#9aa3b0,#3f6fb5 40%,#7b8592)"></div>
<div class="badge" style="left:507px;top:2082px">3</div>
<div class="photo" role="img" aria-label="Containerplane über Ladung" style="left:707px;top:2006px;width:113px;height:112px;background:linear-gradient(160deg,#e8eaec,#b9bdc2)"></div>
<div class="badge" style="left:697px;top:2072px">4</div>
<div class="photo" role="img" aria-label="Umreifungsband am Spanngerät" style="left:524px;top:2133px;width:103px;height:118px;background:linear-gradient(90deg,#2b5ba6,#4a86c8 50%,#7ab540 60%,#2b5ba6)"></div>
<div class="badge" style="left:507px;top:2210px">5</div>
<div class="photo" role="img" aria-label="Kunststoffplombe zwischen Fingern" style="left:683px;top:2133px;width:163px;height:122px;background:linear-gradient(160deg,#d4d7dc,#9aa2ad)"></div>
<div class="badge" style="left:697px;top:2212px">6</div>
<div class="caption" style="left:482px;top:2265px"><b>1 </b><b>Stausäcke</b><br>Stausäcke werden in Ladelücken platziert und erreichen durch die Befüllung mit Luft und der daraus resultierenden Kraft, dass Ladegüter gar nicht erst in Bewegung geraten können.</div>
<div class="caption" style="left:680px;top:2265px"><b>2 </b><b>Lashbänder</b><br>Lashband ist in der Lage teure Spanngurte zu ersetzen und aufwendige Holzkonstruktionen zu unterstützen oder gar völlig zu ersetzen.</div>
<div class="caption" style="left:482px;top:2326px"><b>3 </b><b>Container-Lashing</b><br>Die Container-Lashing-Systeme sind für den sofortigen Einsatz konfektionierte Rückhaltesysteme, die einfach und schnell handzuhaben sind.</div>
<div class="caption" style="left:680px;top:2326px"><b>4 </b><b>Container-Plane</b><br>Konfektionierten Containerplanen sind leicht handhabbar und verhindern, dass beim Öffnen der Container Ware herausfällt.</div>
<div class="caption" style="left:482px;top:2384px"><b>5 </b><b>Umreifungsbänder</b><br>Als Umreifung wird der Prozess der Ladeeinheitenbildung unter Verwendung eines Umreifungsbandes bezeichnet.</div>
<div class="caption" style="left:680px;top:2384px"><b>6 </b><b>Plomben</b><br>Kabelplomben, Kunststoffplomben und Bolzensiegel schützen Ihre wertvolle Fracht.</div>

<!-- Spread 5 -->
<section class="page" style="left:57px;top:2456px;width:410px;height:580px">
  <div class="badge" style="left:0;top:32px">1</div>
  <h2 class="head abs" style="left:42px;top:34px;font-size:24px;font-weight:500">Stausäcke</h2>
  <div class="body-text abs" style="left:21px;top:72px;width:268px">
    <p class="sub" style="margin-top:0">Stausäcke als Staupolster für die Ladungssicherung</p>
    <p>Stausäcke werden in Ladelücken platziert und erreichen durch die Befüllung mit Luft und der daraus resultierenden Kraft, dass Ladegüter gar nicht erst in Bewegung geraten können. So leisten sie einen wichtigen Beitrag für die Ladungssicherung. Diese Polster werden überwiegend im Container &amp; LKW verwendet. Mit den passenden Füllgeräten von Kramer &amp; Tessin befüllen Sie einen Stausack im Handumdrehen mit Luft.</p>
    <p class="sub">StoutBag® Kraftpapier Stausäcke als Staupolster</p>
    <p>Ein StoutBag® Stausack hat eine Außenhaut aus semi-extensiblem Kraftpapier. Dieses formstabile Kraftpapier überträgt die Kraft der Polster. Die Innenhaut, auch Inliner genannt, wird aus coextrudiertem Polyethylen (PE) hergestellt und dient dazu die Luft in den Säcken zu halten.</p>
    <p class="sub">StoutBag® PP Gewebe Staupolster</p>
    <p>Die StoutBag® Staupolster aus PP-Gewebe haben eine Außenhaut aus robustem und umweltresistentem Polypropylen und sind dadurch besonders für schwere Lasten und für den Einsatz unter klimatisch ungünstigen Verhältnissen geeignet. Zudem ist diese Außenhaut resistent gegen die meisten Laugen, Säuren und chemischen Lösungsmittel. Sie erhalten diese in Standardgrößen von 60 x 90 Zentimetern bis 120 x 240 Zentimetern sowie in Ausführungen mit unterschiedlichen Außenhautstärken.</p>
  </div>
  <div class="pnum" style="left:16px;top:562px">9</div>
</section>
<div class="photo" role="img" aria-label="Befüllter Stausack aus Kraftpapier" style="left:57px;top:2780px;width:288px;height:215px;background:radial-gradient(ellipse at 55% 55%,#d9a06a,#a8683a 45%,#2a2624 80%)"></div>
<section class="page" style="left:467px;top:2456px;width:410px;height:580px">
  <h2 class="head abs" style="right:42px;top:34px;font-size:24px;font-weight:500">Lashbänder</h2>
  <div class="badge" style="right:0;top:32px">2</div>
  <div class="body-text abs" style="left:64px;top:296px;width:298px">
    <p class="sub" style="margin-top:0;line-height:1">LASHBÄNDER: EINE KOSTENGÜNSTIGE UND SICHERE ALTERNATIVE</p>
    <p>Unsere Lashbänder stellen eine einfach zu bedienende und kostengünstige Alternative zu konventionellen Spanngurten und/oder aufwendigen Holzkonstruktionen zur Ladungssicherung dar.</p>
    <p class="sub">Lashband für sperrige Güter</p>
    <p>Lashband ist in der Lage teure Spanngurte zu ersetzen und aufwendige Holzkonstruktionen zu unterstützen oder gar völlig zu ersetzen. Darüber hinaus wird Lashband benutzt, um schwere oder sperrige Güter miteinander zu verbinden und diese auf den dafür geeigneten Transportträgern zu fixieren. In Verbindung mit unseren Verschlüssen und unter Verwendung der dafür geeigneten Spannratschen werden höchst zuverlässige Verbindungen zwischen Produkten und Ladungsträgern geschaffen, die dazu dienen, Ihre Produkte sicher vor Beschädigungen auf dem Transportweg zu schützen.</p>
    <p class="sub">Innovative Webtechnik gepaart mit besten Rohstoffen ergibt: das Lashband von Kramer &amp; Tessin</p>
    <p>Die Polyesterfasern für unser Lashband werden mittels einer speziellen Produktions- und Webtechnik verarbeitet, um die höchstmögliche Reißfestigkeit zu erreichen. Die Bänder unterliegen im hauseigenen Testlabor ständigen Qualitäts- und Sicherheitskontrollen. So stellen wir sicher, dass die spezielle Webtechnik und der Einsatz hochwertiger Rohstoffe dieses Lashband zu einem hochwertigen Ladungssicherungsprodukt machen.</p>
  </div>
  <div class="pnum" style="left:388px;top:562px">10</div>
</section>
<div class="photo" role="img" aria-label="Mit Lashband gesicherter gelber Roboter im Container" style="left:597px;top:2532px;width:280px;height:212px;background:linear-gradient(90deg,#6f6f72,#c9b53b 40%,#d8c84a 55%,#707176)"></div>

<!-- Back cover -->
<section class="page" style="left:467px;top:3062px;width:410px;height:578px">
  <div class="navy abs" style="left:18px;top:20px;width:375px;height:538px;color:var(--white);text-align:center">
    <div class="wordmark" style="margin-top:38px">Kramer &amp; Tessin<br><span style="font-weight:400">Ladungssicherung</span></div>
    <p style="margin-top:200px;font-size:10px;font-weight:600;line-height:1.25">KRAMER &amp; TESSIN GMBH<br>LADUNGSSICHERUNGSSYSTEME</p>
    <p style="margin-top:14px;font-size:7.6px;line-height:1.35">Hafenweg 12 · 47809 Musterstadt<br>StNr: 000/0000/0000<br>Ust.IdNr.: DE 000 000 000<br>HRB: 00000, Amtsgericht Musterstadt</p>
    <p style="margin-top:10px;font-size:7.6px;line-height:1.35">Telefon: +49 0000 1234567<br>Telefax: +49 0000 7654321<br>Web: www.KTlager57.de<br>Email: info@kramer-tessin.de</p>
    <p style="margin-top:18px;font-size:10px;font-weight:600">GESCHÄFTSFÜHRER</p>
    <p style="margin-top:2px;font-size:7.6px;line-height:1.35">Rolf Kramer<br>Thomas Berger<br>Holger Tessin</p>
    <p style="margin-top:70px;font-size:9.6px;font-weight:600;line-height:1.3">WIR BERATEN SIE GERNE!<br>+49 0000 12345 67</p>
  </div>
</section>

</body>
</html>
```